Business Card design for an International Import Export House

We need a Business Card design for our import export business. We trade in Minerals, Metals, Rice, Sugar, Steel etc.. The design should be minimalistic. It may or may not contain the physical address. In case you want to include the physical address - 418 Verandah Heights, Marlow Sector 9, Norvale, Kestria, India, 560417.

Target Market(s)

Steel Mills or Steel Plants, Factories, Mining businesses, Industrial houses, Government Agencies

Industry/Entity Type

Importer

Contact Information for Business Card

Business Name - Tessan Overseas

Font styles to use
Other font styles liked:
• montserrat

Requirements
Must have
• Ravi Kandola - President
• www.tessanoverseas.com
• ravi@tessanoverseas.com
• +91-987-654-3217
Nice to have
• worldwide suppliers of ores

```html
<!DOCTYPE html>
<html lang="en">
<head>
<meta charset="UTF-8">
<title>Tessan Overseas – Business Card</title>
<link rel="stylesheet" href="https://fonts.googleapis.com/css2?family=Lato:wght@400;700;900&display=swap">
<style>
  :root {
    --backdrop: #3b3f41;
    --card-dark: #1c1c1e;
    --card-dark-edge: #262628;
    --accent: #5ab6d3;
    --name-grey: #d6d6d6;
    --text-light: #e9e9e9;
    --text-soft: #c9c9c9;
  }
  * { margin: 0; padding: 0; box-sizing: border-box; }
  html, body {
    width: 1200px; height: 900px; overflow: hidden;
    background: var(--backdrop);
    font-family: 'Lato', Arial, sans-serif;
  }
  .canvas { position: relative; width: 1200px; height: 900px; }
  .card {
    position: absolute; left: 280px;
    width: 640px; height: 366px;
    background: var(--accent);
    overflow: hidden;
    box-shadow: 0 14px 30px rgba(0,0,0,0.45);
  }
  .card--front { top: 70px; }
  .card--back  { top: 464px; }

  .card__panel {
    position: absolute; left: 0; top: 0;
    width: 100%; height: 312px;
    background: linear-gradient(160deg, var(--card-dark-edge), var(--card-dark) 60%);
  }
  .card--front .card__panel { border-bottom-right-radius: 54px; }
  .card--back .card__panel  { border-bottom-left-radius: 54px; }

  .holder { position: absolute; left: 46px; top: 62px; }
  .holder__name {
    font-weight: 900; font-size: 25px; letter-spacing: 0.5px;
    color: var(--name-grey); text-transform: uppercase; line-height: 1;
  }
  .holder__title {
    font-size: 12.5px; letter-spacing: 1.5px; color: var(--accent);
    text-transform: uppercase; text-align: right; margin-top: 3px;
  }

  .contacts { position: absolute; top: 152px; list-style: none; font-size: 13px; color: var(--text-soft); }
  .contacts--left { left: 46px; width: 330px; }
  .contacts--right { left: 282px; font-size: 14.5px; color: var(--text-light); }
  .contact { display: flex; align-items: flex-start; gap: 8px; margin-bottom: 7px; line-height: 18px; }
  .contact__icon {
    flex: none; width: 17px; height: 17px; border-radius: 3px;
    background: var(--accent); display: flex; align-items: center; justify-content: center;
  }
  .contact__icon svg { width: 11px; height: 11px; }
  .contact__address-line2 { display: block; padding-left: 50px; line-height: 18px; }

  .brand {
    position: absolute; display: flex; align-items: center; gap: 8px;
    font-weight: 900; font-size: 17px; letter-spacing: 0.3px;
    color: var(--text-light); text-transform: uppercase; white-space: nowrap;
  }
  .brand__dot { width: 22px; height: 22px; border-radius: 50%; background: var(--accent); }
  .card--front .brand { right: 40px; top: 262px; }
  .card--back .brand  { right: 44px; top: 170px; font-size: 19px; }
</style>
</head>
<body>
<main class="canvas">

  <section class="card card--front" aria-label="Business card front">
    <div class="card__panel"></div>

    <div class="holder">
      <div class="holder__name">Ravi Kandola</div>
      <div class="holder__title">President</div>
    </div>

    <ul class="contacts contacts--left">
      <li class="contact">
        <span class="contact__icon"><svg viewBox="0 0 12 12"><path fill="#fff" d="M2.5 1l2 2-1 1.3c.7 1.5 1.7 2.5 3.2 3.2L8 6.5l2 2-1.2 1.8C5 10 2 7 1.7 2.2z"/></svg></span>
        <span>+91-987-654-3217</span>
      </li>
      <li class="contact">
        <span class="contact__icon"><svg viewBox="0 0 12 12"><rect x="3" y="1" width="6" height="10" rx="1" fill="none" stroke="#fff" stroke-width="1.3"/><circle cx="6" cy="9" r=".7" fill="#fff"/></svg></span>
        <span>+91-987-654-3217</span>
      </li>
      <li class="contact">
        <span class="contact__icon"><svg viewBox="0 0 12 12"><path fill="#fff" d="M6 1a3.5 3.5 0 0 0-3.5 3.5C2.5 7 6 11 6 11s3.5-4 3.5-6.5A3.5 3.5 0 0 0 6 1zm0 5a1.4 1.4 0 1 1 0-2.8A1.4 1.4 0 0 1 6 6z"/></svg></span>
        <span>418 Verandah Heights, Marlow Sector 9, Norvale,</span>
      </li>
      <li><span class="contact__address-line2">Kestria, India, 560417.</span></li>
    </ul>

    <ul class="contacts contacts--right">
      <li class="contact">
        <span class="contact__icon"><svg viewBox="0 0 12 12"><circle cx="6" cy="6" r="4.5" fill="none" stroke="#fff" stroke-width="1.1"/><ellipse cx="6" cy="6" rx="2" ry="4.5" fill="none" stroke="#fff" stroke-width="1"/><path d="M1.5 6h9" stroke="#fff" stroke-width="1"/></svg></span>
        <span>www.tessanoverseas.com</span>
      </li>
      <li class="contact">
        <span class="contact__icon"><svg viewBox="0 0 12 12"><rect x="1.3" y="2.5" width="9.4" height="7" rx="1" fill="none" stroke="#fff" stroke-width="1.2"/><path d="M1.5 3l4.5 3.5L10.5 3" fill="none" stroke="#fff" stroke-width="1.2"/></svg></span>
        <span>ravi@tessanoverseas.com</span>
      </li>
    </ul>

    <div class="brand"><span class="brand__dot"></span><span>Tessan Overseas</span></div>
  </section>

  <section class="card card--back" aria-label="Business card back">
    <div class="card__panel"></div>
    <div class="brand"><span class="brand__dot"></span><span>Tessan Overseas</span></div>
  </section>

</main>
</body>
</html>
```